Bubble map/flip book

I need someone to create a bubble map with explanations using the attached. This will be used to create a color coded flip book/manual. I need you to clean this up.

Dorothywinslade@postlark.com

```html
<!DOCTYPE html>
<html lang="en">
<head>
<meta charset="utf-8">
<title>Claim Denial Flip Book Pages</title>
<link rel="stylesheet" href="https://fonts.googleapis.com/css2?family=Roboto:wght@400;700;900&display=swap">
<style>
  :root {
    --bg: #fbfbfb;
    --page: #ffffff;
    --red: #e3161e;
    --red-dark: #b50f15;
    --yellow: #ffd21a;
    --orange: #f7a21b;
    --orange-deep: #f08a00;
    --box: #ffc82c;
    --line: #f3a41c;
    --ink: #333333;
    --c-yellow: #ffc21a;
    --c-orange: #f7931e;
    --c-pink: #e83e8c;
    --c-orange2: #f26522;
    --c-purple: #8e3bd6;
    --c-red: #e3161e;
    --c-blue: #2f6fd1;
  }
  * { box-sizing: border-box; margin: 0; padding: 0; }
  html, body { width: 887px; height: 1200px; overflow: hidden; }
  body { background: var(--bg); font-family: "Roboto", Arial, sans-serif; position: relative; color: var(--ink); }

  .page {
    position: absolute; left: 240px; width: 415px; height: 548px;
    background: linear-gradient(160deg, #ffffff 40%, #eeeeee);
    box-shadow: 0 3px 10px rgba(0,0,0,.18);
    overflow: hidden;
  }
  .page--denial { top: 28px; }
  .page--referral { top: 622px; }
  .page__band { position: absolute; left: 0; top: 0; width: 100%; height: 20px; }
  .page--denial .page__band { background: var(--red); }
  .page--referral .page__band { background: var(--yellow); }
  .page__corner { position: absolute; right: 0; bottom: 0; width: 46px; height: 46px; }
  .page__links { position: absolute; left: 0; top: 0; }

  .title-pill {
    position: absolute; display: flex; align-items: center; justify-content: center;
    text-align: center; border-radius: 30px; font-weight: 900;
  }
  .page--denial .title-pill {
    left: 88px; top: 108px; width: 240px; height: 46px;
    background: var(--red); color: #fff; font-size: 16px; letter-spacing: .5px;
    box-shadow: 0 0 0 4px #fff, 0 0 0 6px var(--red), 0 3px 8px rgba(0,0,0,.3);
  }
  .page--referral .title-pill {
    left: 82px; top: 50px; width: 250px; height: 44px;
    background: linear-gradient(var(--orange), var(--orange-deep)); color: #fff;
    font-size: 13px; line-height: 1.2; padding: 0 16px;
    box-shadow: 0 0 0 4px #fff, 0 0 0 6px var(--yellow), 0 3px 8px rgba(0,0,0,.25);
  }

  .reason {
    position: absolute; width: 78px; height: 78px; border-radius: 50%;
    background: #fff; border: 7px solid var(--ring);
    box-shadow: 0 0 0 2px #fff, 0 0 0 3px var(--ring), 0 3px 6px rgba(0,0,0,.25);
    display: flex; align-items: center; justify-content: center; text-align: center;
    font-family: "Roboto", Arial, sans-serif; font-size: 9.5px; font-weight: 700; line-height: 1.15; padding: 4px;
  }

  .flow-box {
    position: absolute; background: var(--box); border: 2px solid #fff;
    box-shadow: 0 0 0 1px var(--line), 0 2px 5px rgba(0,0,0,.2);
    color: #fff; font-size: 8px; line-height: 1.3; text-align: center;
    display: flex; align-items: center; justify-content: center; padding: 6px;
  }
  .flow-box--outlined { background: #fff; color: var(--orange-deep); border: 3px solid var(--box); }
  .flow-box--stack { border-top: 10px solid var(--orange); }
</style>
</head>
<body>

<section class="page page--denial">
  <div class="page__band"></div>
  <svg class="page__links" width="415" height="548" viewBox="0 0 415 548">
    <g stroke="#9a9a9a" stroke-width="2" fill="none">
      <line x1="40" y1="131" x2="40" y2="228"/>
      <line x1="40" y1="131" x2="88" y2="131"/>
      <line x1="138" y1="154" x2="138" y2="228"/>
      <line x1="256" y1="154" x2="256" y2="228"/>
      <line x1="356" y1="131" x2="356" y2="228"/>
      <line x1="328" y1="131" x2="356" y2="131"/>
      <line x1="90" y1="154" x2="90" y2="302"/>
      <line x1="197" y1="154" x2="197" y2="302"/>
      <line x1="306" y1="154" x2="306" y2="302"/>
    </g>
  </svg>
  <div class="title-pill">CLAIM HAS DENIED</div>

  <div class="reason" style="--ring: var(--c-yellow); left: 1px; top: 228px;">Auth/ Referral needed</div>
  <div class="reason" style="--ring: var(--c-orange); left: 99px; top: 228px;">Duplicate</div>
  <div class="reason" style="--ring: var(--c-pink); left: 217px; top: 228px;">Global Inclusive</div>
  <div class="reason" style="--ring: var(--c-orange2); left: 317px; top: 228px;">Past timely Filling</div>
  <div class="reason" style="--ring: var(--c-purple); left: 51px; top: 302px;">Coding/ Billing Errors</div>
  <div class="reason" style="--ring: var(--c-red); left: 158px; top: 302px;">Base Covered Charge</div>
  <div class="reason" style="--ring: var(--c-blue); left: 267px; top: 302px;">Additional Information Requested</div>

  <svg class="page__corner" viewBox="0 0 46 46"><polygon points="46,0 46,46 0,46" fill="var(--red)"/><polygon points="46,0 0,46 30,30" fill="var(--red-dark)"/></svg>
</section>

<section class="page page--referral">
  <div class="page__band"></div>
  <svg class="page__links" width="415" height="548" viewBox="0 0 415 548">
    <g stroke="var(--line)" stroke-width="2" fill="none">
      <line x1="200" y1="176" x2="200" y2="200"/>
      <line x1="100" y1="200" x2="300" y2="200"/>
      <line x1="100" y1="200" x2="100" y2="220"/>
      <line x1="300" y1="200" x2="300" y2="220"/>
      <line x1="100" y1="318" x2="100" y2="350"/>
      <line x1="66" y1="350" x2="143" y2="350"/>
      <line x1="66" y1="350" x2="66" y2="382"/>
      <line x1="143" y1="350" x2="143" y2="382"/>
      <line x1="300" y1="318" x2="300" y2="350"/>
      <line x1="262" y1="350" x2="340" y2="350"/>
      <line x1="262" y1="350" x2="262" y2="382"/>
      <line x1="340" y1="350" x2="340" y2="382"/>
    </g>
  </svg>
  <div class="title-pill">Claim denied for no authorization/ referral</div>

  <div class="flow-box" style="left: 140px; top: 116px; width: 124px; height: 60px;">Contact provider office and request the referral on file</div>

  <div class="flow-box flow-box--outlined" style="left: 32px; top: 220px; width: 136px; height: 98px;">Does the patient need authorization or a referral? Review the plan benefits to confirm the requirement</div>
  <div class="flow-box flow-box--outlined" style="left: 232px; top: 220px; width: 136px; height: 98px;">If the service is not covered, contact the plan to confirm coverage details. If authorization exists resubmit the claim</div>

  <div class="flow-box flow-box--stack" style="left: 32px; top: 382px; width: 68px; height: 96px;">Request a retro authorization from the provider office then resubmit</div>
  <div class="flow-box flow-box--stack" style="left: 114px; top: 382px; width: 58px; height: 96px;">Submit an appeal request</div>
  <div class="flow-box flow-box--stack" style="left: 232px; top: 382px; width: 60px; height: 96px;">Contact the health plan to verify status</div>
  <div class="flow-box flow-box--stack" style="left: 306px; top: 382px; width: 68px; height: 96px;">Resubmit the claim with the referral number to claims team</div>

  <svg class="page__corner" viewBox="0 0 46 46"><polygon points="46,0 46,46 0,46" fill="var(--yellow)"/><polygon points="46,0 0,46 30,30" fill="var(--orange)"/></svg>
</section>

</body>
</html>
```